Business Card Design Project

We have a logo design and are now looking for a business card design. We supply pre-construction services to the Wireless Telecommunication Industry in the development of cell phone tower and other antenna supporting infrastructure e.g. buildings. The types of services include Real Estate Leasing, Zoning & Permitting,Surveying and A&E work. I am looking for a card that includes the logo we have selected along with the full company name. Company colors are Blue and Silver. I want something professional and that "pops". Use your imagination with the four sided star portion of the logo - it can be stretched such that it occupies a large portion of the card or kept simple the way it is. I am interested in seeing the design on a white, silver, navy, black or charcoal background or any other color you think works well with the logo. Apart from the logo that includes LNI we also need to see the full company name on the card - Lanternway Networks, Inc. The design must also show a persons name, title, address, (2) phone numbers, e-mail address and web address www.lni-sample.co

Target Market(s)

Cell phone carriers e.g. Coravent Mobile, QB&R, K-Cellix, Dunmo etc.

Industry/Entity Type

Cell Phone

Requirements
Must have
• Logo and
Lanternway Networks, Inc.

```html
<!DOCTYPE html>
<html lang="en">
<head>
<meta charset="UTF-8">
<title>LNI Business Card</title>
<link rel="stylesheet" href="https://fonts.googleapis.com/css2?family=Open+Sans:wght@400;600;700&display=swap">
<style>
  :root {
    --page-bg: #eef0f3;
    --card-bg: #ffffff;
    --card-shade: #f1f2f4;
    --brand-blue: #1f7fd0;
    --brand-blue-deep: #1565b0;
    --brand-steel: #7d8894;
    --ink-dark: #2b2f36;
    --ink-mid: #3c424a;
    --divider: #2f3338;
  }
  * { margin: 0; padding: 0; box-sizing: border-box; }
  html, body {
    width: 1200px;
    height: 900px;
    overflow: hidden;
    background: var(--page-bg);
    font-family: "Open Sans", Arial, sans-serif;
  }
  .canvas {
    width: 1200px;
    height: 900px;
    display: flex;
    align-items: center;
    justify-content: center;
  }
  .business-card {
    position: relative;
    width: 980px;
    height: 560px;
    border-radius: 44px;
    background: linear-gradient(180deg, var(--card-bg) 0%, var(--card-shade) 100%);
    box-shadow: 0 18px 40px rgba(30, 40, 55, 0.14);
    overflow: hidden;
  }
  .brand-mark {
    position: absolute;
    top: 52px;
    left: 0;
    width: 100%;
    display: flex;
    align-items: center;
    justify-content: center;
    gap: 30px;
  }
  .brand-dot {
    width: 116px;
    height: 116px;
    border-radius: 50%;
    background: var(--brand-blue);
  }
  .brand-name {
    font-size: 140px;
    font-weight: 700;
    line-height: 1;
    letter-spacing: 6px;
    color: var(--brand-blue-deep);
  }
  .company-name {
    position: absolute;
    top: 200px;
    left: 0;
    width: 100%;
    text-align: center;
    font-size: 22px;
    font-weight: 600;
    letter-spacing: 3px;
    text-transform: uppercase;
    color: var(--brand-steel);
  }
  .brand-band {
    position: absolute;
    top: 250px;
    left: 0;
    width: 100%;
    height: 16px;
    background: var(--brand-blue);
  }
  .contact-block {
    position: absolute;
    top: 304px;
    left: 0;
    width: 100%;
    display: flex;
    justify-content: center;
  }
  .person {
    width: 330px;
    padding-right: 34px;
    padding-top: 26px;
    text-align: right;
  }
  .person-name {
    font-size: 32px;
    font-weight: 700;
    color: var(--brand-blue);
  }
  .person-title {
    margin-top: 8px;
    font-size: 22px;
    font-weight: 600;
    color: var(--ink-dark);
  }
  .divider {
    width: 2px;
    height: 204px;
    background: var(--divider);
  }
  .details {
    list-style: none;
    padding-left: 30px;
    width: 500px;
  }
  .details li {
    display: flex;
    align-items: center;
    gap: 12px;
    height: 40px;
    font-size: 23px;
    color: var(--ink-mid);
    white-space: nowrap;
  }
  .details svg {
    width: 26px;
    height: 26px;
    flex: none;
    fill: var(--brand-blue);
  }
</style>
</head>
<body>
<main class="canvas">
  <section class="business-card" aria-label="Lanternway Networks, Inc. business card">
    <header class="brand-mark">
      <span class="brand-dot" aria-hidden="true"></span>
      <span class="brand-name">LNI</span>
    </header>
    <p class="company-name">Lanternway Networks, Inc.</p>

    <div class="brand-band" aria-hidden="true"></div>

    <div class="contact-block">
      <div class="person">
        <p class="person-name">Dana Whitlow</p>
        <p class="person-title">Manager</p>
      </div>
      <div class="divider" aria-hidden="true"></div>
      <ul class="details">
        <li>
          <svg viewBox="0 0 24 24" aria-hidden="true"><path d="M6.6 10.8a15.1 15.1 0 0 0 6.6 6.6l2.2-2.2a1 1 0 0 1 1-.25 11.4 11.4 0 0 0 3.6.57 1 1 0 0 1 1 1V20a1 1 0 0 1-1 1A17 17 0 0 1 3 4a1 1 0 0 1 1-1h3.5a1 1 0 0 1 1 1c0 1.25.2 2.45.57 3.6a1 1 0 0 1-.25 1z"/></svg>
          555.014.2685
        </li>
        <li>
          <svg viewBox="0 0 24 24" aria-hidden="true"><path d="M6.6 10.8a15.1 15.1 0 0 0 6.6 6.6l2.2-2.2a1 1 0 0 1 1-.25 11.4 11.4 0 0 0 3.6.57 1 1 0 0 1 1 1V20a1 1 0 0 1-1 1A17 17 0 0 1 3 4a1 1 0 0 1 1-1h3.5a1 1 0 0 1 1 1c0 1.25.2 2.45.57 3.6a1 1 0 0 1-.25 1z"/></svg>
          555.018.3451
        </li>
        <li>
          <svg viewBox="0 0 24 24" aria-hidden="true"><path d="M2 5h20v14H2z M4 7v.5l8 5 8-5V7l-8 5z" fill-rule="evenodd"/></svg>
          dana@lni-sample.co
        </li>
        <li>
          <svg viewBox="0 0 24 24" aria-hidden="true"><path d="M12 3 2 12h3v9h5v-6h4v6h5v-9h3z"/></svg>
          4820 Ridgeview Lane, Harlow, TX 77999
        </li>
        <li>
          <svg viewBox="0 0 24 24" aria-hidden="true"><path d="M12 2a10 10 0 1 0 0 20 10 10 0 0 0 0-20zm6.9 9h-3a15 15 0 0 0-1.2-5.6A8 8 0 0 1 18.9 11zM12 4.1c.9 1.2 1.8 3.5 1.9 6.9h-3.8c.1-3.4 1-5.7 1.9-6.9zM9.3 5.4A15 15 0 0 0 8.1 11h-3a8 8 0 0 1 4.2-5.6zM5.1 13h3a15 15 0 0 0 1.2 5.6A8 8 0 0 1 5.1 13zm6.9 6.9c-.9-1.2-1.8-3.5-1.9-6.9h3.8c-.1 3.4-1 5.7-1.9 6.9zm2.7-1.3a15 15 0 0 0 1.2-5.6h3a8 8 0 0 1-4.2 5.6z"/></svg>
          www.lni-sample.co
        </li>
      </ul>
    </div>
  </section>
</main>
</body>
</html>
```